Company Web Design Project

Velmora links works in the market of renewable energy with energy monitoring systems.

Velmora-link wants a light and easy company website that informs about our core business and our products as well as the company. The sites should work on multiple platforms. It should include pictures and possibilities for news.
You find elements and company information on the following links:

http://velmora-link.example/english-version/index.htm
some productinformation you find on this site:
http://quorvane.example/

Velmora-link AG is also interested in a Powerpoint template that matches the new website design as well as businesscards and a letter template.

Some more information about the company.

Headquartered in Karlsruhe, Germany, Velmora-Link AG manufactures hardware & software solutions for remote monitoring, analysis, and control of electrical installations, alarm systems, and other critical networks.

In addition, our company provides test, measurement, and control equipment for use in a wide range of industrial and biological processes.

Founded in the year 2000, Velmora-Link AG has established a comprehensive service network. Our solutions and systems are in operation e.g. in Europe, USA, Brazil, and Asia.

Velmora-Link's team of experienced engineers, physicists, and network specialists continuously develop innovative solutions for many key industries - particularly in the renewable energies field.

To ensure the operational safety of their plants by means of optimized real time fault analysis routines

for process optimization

for a measurable increase in yield from production and trade.

Our products are distributed globally via an international dealer network.

In the interest of our customers and their needs, our aim is to expand this dealer network even more.

Target Market(s)

large solar project companies like, large renewable energy investors, large wholesellers for renewable energy, producer of solar panels.

Industry/Entity Type

Electrical

Requirements
Must have
• responsive design for multiple platforms

```html
<!DOCTYPE html>
<html lang="de">
<head>
<meta charset="utf-8">
<title>Velmora – Home</title>
<link href="https://fonts.googleapis.com/css2?family=Open+Sans:wght@400;600;700&display=swap" rel="stylesheet">
<style>
:root{
  --teal:#2aa893;
  --teal-dark:#1f8f7c;
  --ink:#2b2b2b;
  --muted:#555;
  --paper:#f1f1f1;
  --line:#dedede;
  --footer:#3b3b3b;
}
*{box-sizing:border-box;margin:0;padding:0}
html,body{width:1200px;height:1000px;overflow:hidden}
body{font-family:"Open Sans",Arial,sans-serif;background:var(--paper);color:var(--ink);position:relative}
.topbar{position:absolute;top:0;left:0;width:1200px;height:6px;background:var(--teal-dark)}
.header{position:absolute;top:6px;left:0;width:1200px;height:104px;background:#fff;border-bottom:1px solid #e6e6e6}
.header-rule{position:absolute;top:0;left:0}
.brand{position:absolute;left:118px;top:26px;display:flex;align-items:center;gap:12px}
.brand-mark{width:48px;height:48px;background:var(--teal-dark)}
.brand-name{font-size:32px;font-weight:700;color:var(--ink);letter-spacing:-.3px}
.nav{position:absolute;left:415px;top:44px;display:flex;font-size:14px;font-weight:700;color:#333}
.nav a{color:inherit;text-decoration:none}
.nav .active{color:var(--teal)}
.nav-tab{position:absolute;left:406px;top:0;width:59px;height:8px;background:var(--teal-dark)}
.hero{position:absolute;top:117px;left:0;width:1200px;height:325px;background:linear-gradient(180deg,#a9b9c6 0%,#6f7f6a 30%,#4a5e8e 60%,#3b4f88 100%)}
.card{position:absolute;top:380px;width:316px;height:227px;border:1px solid #e4e4e4;background:transparent}
.card-title{position:absolute;left:7px;top:7px;width:300px;height:55px;background:var(--teal);color:#fff;font-weight:700;display:flex;align-items:center;justify-content:center;font-size:24px}
.card-title.small{font-size:18px}
.card-media{position:absolute;left:7px;top:62px;width:300px;height:158px}
.card-more{position:absolute;left:237px;top:182px;width:93px;height:30px;background:var(--teal);color:#fff;font-size:15px;display:flex;align-items:center;justify-content:center}
.card-more::after{content:"";position:absolute;right:0;top:-8px;border-left:12px solid var(--teal-dark);border-top:8px solid transparent}
.section-title{position:absolute;top:626px;font-size:23px;color:#333;display:flex;align-items:center;gap:8px}
.section-title::after{content:"";display:block;height:14px;background:#fff;flex:1}
.panel{position:absolute;top:668px;height:245px;background:#fff;box-shadow:0 1px 3px rgba(0,0,0,.12)}
.news-item{height:83px;border-bottom:1px solid var(--line);display:flex;margin:0 8px 0 0}
.news-item:last-child{border-bottom:none}
.news-date{width:74px;text-align:center;color:var(--teal-dark);font-size:16px;line-height:21px;padding-top:18px}
.news-body{padding-top:12px}
.news-day{font-size:17px;color:#444;margin-bottom:5px}
.news-text{font-size:11.5px;color:#555;line-height:15px;width:372px}
.links{display:grid;grid-template-columns:165px 154px 161px;grid-template-rows:84px 80px 81px}
.link{border-right:1px solid var(--line);border-bottom:1px solid var(--line);display:flex;flex-direction:column;align-items:center;justify-content:center;gap:2px;font-size:14px;color:#333}
.link:nth-child(3n){border-right:none}
.link:nth-child(n+7){border-bottom:none}
.link svg{width:34px;height:30px}
.footer{position:absolute;top:947px;left:0;width:1200px;height:53px;background:var(--footer)}
.social{position:absolute;left:111px;top:12px;display:flex;gap:6px}
.social span{width:27px;height:27px;border-radius:5px;background:#6d6d6d}
.copyright{position:absolute;right:110px;top:19px;color:#cfcfcf;font-size:13px}
</style>
</head>
<body>
<div class="topbar"></div>
<header class="header">
  <svg class="header-rule" width="1200" height="60" aria-hidden="true">
    <polyline points="70,6 70,52 104,52" fill="none" stroke="#555" stroke-width="1"/>
    <circle cx="105" cy="52" r="3" fill="#555"/>
    <polyline points="1128,6 1128,52 1094,52" fill="none" stroke="#555" stroke-width="1"/>
    <circle cx="1093" cy="52" r="3" fill="#555"/>
  </svg>
  <div class="brand"><span class="brand-mark"></span><span class="brand-name">Velmora</span></div>
  <nav class="nav">
    <a class="active" href="#" style="width:76px">HOME</a>
    <a href="#" style="width:112px">COMPANY</a>
    <a href="#" style="width:114px">BUSINESS</a>
    <a href="#" style="width:119px">PRODUCTS</a>
    <a href="#" style="width:95px">TOPICAL</a>
    <a href="#">SERVICE &amp; CONTACT</a>
  </nav>
</header>
<div class="nav-tab"></div>
<div class="hero" role="img" aria-label="Rooftop covered with rows of solar panels, forested hills behind"></div>

<section class="card" style="left:110px">
  <div class="card-title">NEW PRODUCTS</div>
  <div class="card-media" role="img" aria-label="Golden egg in a nest on a dark teal background" style="background:linear-gradient(120deg,#2c5a52,#5c8a80 60%,#d8c9a0)"></div>
  <div class="card-more">More</div>
</section>
<section class="card" style="left:442px">
  <div class="card-title">PRESS REVIEW</div>
  <div class="card-media" role="img" aria-label="Illustrated rolled newspaper with news headline" style="background:linear-gradient(160deg,#f4f6f9,#c9d6e4)"></div>
  <div class="card-more">More</div>
</section>
<section class="card" style="left:774px">
  <div class="card-title small">LOCATION AND DIRECTIONS</div>
  <div class="card-media" role="img" aria-label="Street map showing the company location" style="background:linear-gradient(135deg,#e6e2da,#cfd8e0)"></div>
  <div class="card-more">More</div>
</section>

<h2 class="section-title" style="left:110px;width:475px;font-weight:400">What's New?</h2>
<div class="panel" style="left:110px;width:476px">
  <div class="news-item"><div class="news-date">29<br>May</div><div class="news-body"><div class="news-day">Donnerstag,</div><div class="news-text">Die Steigerung der Endenergieeffizienz stellt die kostengünstigste und sinnvollste Brückentechnologie in ein regeneratives</div></div></div>
  <div class="news-item"><div class="news-date">29<br>May</div><div class="news-body"><div class="news-day">Dienstag</div><div class="news-text">Eis und Schnee können PV-Anlagen erheblich in ihrer Leistungsfähigkeit beeinträchtigen oder gar beschädigen. erat</div></div></div>
  <div class="news-item"><div class="news-date">29<br>May</div><div class="news-body"><div class="news-day">Dienstag</div><div class="news-text">Anfang des Jahres trat eine weitere Novelle des "Erneuerbare Energien Gesetzes" (EEG) in Kraft. erat  dolore magna aliquam erat</div></div></div>
</div>

<h2 class="section-title" style="left:610px;width:480px;font-weight:400">Quick Links</h2>
<div class="panel links" style="left:610px;width:480px">
  <div class="link"><svg viewBox="0 0 34 30"><path d="M17 3a7 7 0 0 0-7 7c0 6 7 13 7 13s7-7 7-13a7 7 0 0 0-7-7z" fill="#555"/><circle cx="17" cy="10" r="2.5" fill="#fff"/></svg>Your Nearest Dealer</div>
  <div class="link"><svg viewBox="0 0 34 30"><circle cx="17" cy="15" r="13" fill="#555"/><path d="M10 11h14l-2 7h-10z" fill="#fff"/></svg>Registering</div>
  <div class="link"><svg viewBox="0 0 34 30"><circle cx="17" cy="15" r="13" fill="#444"/><path d="M13 8h8v7h4l-8 8-8-8h4z" fill="#fff"/></svg>Download</div>
  <div class="link"><svg viewBox="0 0 34 30"><circle cx="17" cy="15" r="12" fill="none" stroke="#222" stroke-width="2.5"/><text x="17" y="21" font-size="16" font-weight="700" text-anchor="middle" fill="#222" font-family="Open Sans, sans-serif">?</text></svg>FAQ</div>
  <div class="link"><svg viewBox="0 0 34 30"><circle cx="17" cy="15" r="13" fill="#555"/><rect x="10" y="9" width="14" height="12" fill="#fff"/><rect x="10" y="9" width="14" height="3" fill="#999"/></svg>Dates</div>
  <div class="link"><svg viewBox="0 0 34 30"><rect x="6" y="8" width="18" height="18" fill="none" stroke="#333" stroke-width="2"/><path d="M10 16l5 6 13-19" fill="none" stroke="#333" stroke-width="3"/></svg>Press Release</div>
  <div class="link"><svg viewBox="0 0 34 30"><rect x="8" y="3" width="18" height="24" rx="2" fill="none" stroke="#333" stroke-width="2"/><path d="M12 10h10M12 15h10M12 20h10" stroke="#333" stroke-width="2"/></svg>Contact form</div>
  <div class="link"><svg viewBox="0 0 34 30"><path d="M2 12l8-5 7 4 7-4 8 5-6 6-9 5-9-5z" fill="#555"/></svg>Contact Partners</div>
  <div class="link"><svg viewBox="0 0 34 30"><rect x="5" y="10" width="17" height="17" rx="2" fill="#555"/><path d="M16 4h12v12l-4-4-7 7-4-4 7-7z" fill="#333"/></svg>External Link</div>
</div>

<footer class="footer">
  <div class="social"><span></span><span></span><span></span></div>
  <div class="copyright">@ Copyright 2013 Velmora link. All Rights Reserved.</div>
</footer>
</body>
</html>
```